Serial Entrepreneur Business Card: 4 Logo Design

I am a serial entrepreneur and a full time mechanical engineer. I have four businesses. I would like to display them all on one business card.
*Please see the attached PDF for the design requirements*

www.KelbroNest.com

Businesses
-KelbroNest
-Quiet Lantern Properties
-Torlen Products
-Drosk Harbor Cast

Target Market(s)

Clients, Entrepreneurs, Associates, really anyone. Should be very professional.

Industry/Entity Type

Entrepreneur

Contact Information for Business Card

3.5" x 2" Standard Business Card Size
** Please review the attached requirement PDF for in depth detail on what I am expecting**

Font styles to use
Sans Serif

Requirements
Must have
• My personal contact information:
• First Name: Dae hwan
• Last Name: Pellow
• Nick Name: Riko
• Address: 83 Tolmer Court, Garfield NJ 07392
• Phone Number: 201-574-2916
• Email: RikodPellow@mailnest.example
• Website: www.KelbroNest.com
• All Four Logos of the Companies I own:
• -KelbroNest
• -Quiet Lantern Properties
• -Torlen Products
• -Drosk Harbor Cast
• My Professions:
• -Prototyping Engineer
• -Real Estate Investor
• -Financial Blogger
• -Video Podcaster
• -Online Retail Seller
Nice to have
• If it fits, please include the website for each logo, if there is more space please include the email for each.
• It might be nice to have the QX GUILD Logo, or TOVRA logo for my full-time job. But only if it fits.

```html
<!DOCTYPE html>
<html lang="en">
<head>
<meta charset="utf-8">
<title>Dae hwan "Riko" Pellow — Business Card</title>
<link href="https://fonts.googleapis.com/css2?family=Roboto:wght@400;500;700&display=swap" rel="stylesheet">
<style>
  :root{
    --bg:#2d2623;
    --card-dark:#2b2d2c;
    --band-black:#0b0b0b;
    --white:#ffffff;
    --text-light:#e4e4e4;
    --cell-gray:#a9a9a9;
    --cell-light:#e7e7e9;
    --ink:#1c1c1c;
    --accent-green:#2f8f45;
  }
  *{margin:0;padding:0;box-sizing:border-box}
  html,body{width:1200px;height:1000px;overflow:hidden}
  body{background:var(--bg);position:relative;font-family:"Roboto",Arial,sans-serif}

  /* Front card */
  .card-front{
    position:absolute;left:160px;top:185px;width:580px;height:330px;
    background:var(--card-dark);overflow:hidden;
    box-shadow:0 6px 18px rgba(0,0,0,.45);
  }
  .front-band{position:absolute;left:0;top:0;width:100%;height:128px;background:var(--band-black)}
  .front-rule{position:absolute;left:0;top:128px;width:100%;height:6px;background:var(--white)}
  .owner-name{
    position:absolute;left:34px;top:88px;color:var(--white);
    font-weight:700;font-size:20px;letter-spacing:.2px;
  }
  .employer-mark{
    position:absolute;right:48px;top:96px;width:72px;height:72px;
    background:var(--white);border:4px solid var(--band-black);border-radius:8px;
    display:flex;align-items:center;justify-content:center;
    font-weight:700;font-size:12px;color:var(--band-black);text-align:center;line-height:1.1;
  }
  .professions{
    position:absolute;left:60px;top:205px;color:var(--text-light);
    font-size:15px;line-height:21px;
  }
  .front-divider{position:absolute;left:245px;top:200px;width:1px;height:110px;background:var(--text-light)}
  .contact-list{
    position:absolute;left:270px;top:180px;color:var(--text-light);
    font-size:15px;line-height:20px;list-style:none;
  }

  /* Back card */
  .card-back{
    position:absolute;left:485px;top:530px;width:525px;height:300px;
    background:var(--band-black);padding:18px 0;
    box-shadow:0 6px 18px rgba(0,0,0,.45);
  }
  .venture-grid{display:grid;grid-template-columns:1fr 1fr;grid-template-rows:1fr 1fr;height:100%}
  .venture{
    display:flex;flex-direction:column;align-items:center;justify-content:flex-end;
    padding:0 10px 12px;min-width:0;overflow:hidden;text-align:center;
    color:var(--ink);font-size:13px;letter-spacing:.6px;line-height:17px;
  }
  .venture--gray{background:var(--cell-gray)}
  .venture--light{background:var(--cell-light)}
  .venture-name{
    display:flex;align-items:center;justify-content:center;gap:7px;margin-bottom:14px;
    max-width:100%;white-space:nowrap;
    font-weight:700;font-size:16px;letter-spacing:0;color:var(--ink);
  }
  .venture-name .mark{flex:0 0 auto;width:16px;height:16px;background:var(--ink)}
  .venture-name--green{color:var(--accent-green)}
  .venture-name--green .mark{background:var(--accent-green)}
</style>
</head>
<body>

<section class="card-front" aria-label="Business card front">
  <div class="front-band"></div>
  <div class="front-rule"></div>
  <h1 class="owner-name">Dae hwan “Riko” Pellow</h1>
  <div class="employer-mark">QX<br>GUILD</div>
  <div class="professions">
    Prototyping Engineer<br>
    Real Estate Investor<br>
    Financial Blogger<br>
    Video Podcaster<br>
    Online Retail Seller
  </div>
  <div class="front-divider"></div>
  <ul class="contact-list">
    <li>201-574-2916</li>
    <li>RikodPellow@mailnest.example</li>
    <li>Riko@KelbroNest.com</li>
    <li>www.KelbroNest.com</li>
    <li>83 Tolmer Court, Garfield NJ 07392</li>
  </ul>
</section>

<section class="card-back" aria-label="Business card back">
  <div class="venture-grid">
    <div class="venture venture--gray">
      <div class="venture-name"><span class="mark"></span>KelbroNest</div>
      <span>www.KelbroNest.com</span>
      <span>Riko@KelbroNest.com</span>
    </div>
    <div class="venture venture--light">
      <div class="venture-name venture-name--green"><span class="mark"></span>Drosk Harbor Cast</div>
      <span>www.DroskHarborCast.com</span>
      <span>Media@DroskHarborCast.com</span>
    </div>
    <div class="venture venture--light">
      <div class="venture-name"><span class="mark"></span>Torlen Products</div>
      <span>www.TorlenProducts.com</span>
      <span>Sales@TorlenProducts.com</span>
    </div>
    <div class="venture venture--gray">
      <div class="venture-name"><span class="mark"></span>Quiet Lantern Properties</div>
      <span>www.QuietLanternProperties.com</span>
      <span>Riko@QuietLanternProperties.com</span>
    </div>
  </div>
</section>

</body>
</html>
```